Cruise Booking Website

Cruise search and booking website

This project is a redesign of a cruise booking website we did a few years ago.

The current website is located here: http://voyage.pelnarix.com/en/

It's not fully functional but gives you ad idea how miserable the old design was.

All the information about cruises, cruise lines, destinations, ports and shore excursions will be similar to http://www.velmoravo.com/
Actual search pages (form, results, single result, sailing and cabin selection, ship info, booking) will have EXACTLY the same info as velmoravo.com

We like the style of http://harbortolvanex.com, it's quite modern, good spacing, not overloaded with information. So you can use it as an example of what we like, not what we want as a final result for us. Please, don't copy it. The result should not be possible to resemble the harbortolvanex.com, because our site has to be unique. This is important!
If you submit a design that clearly reminds another cruise site it will be rejected!

Also the mockup provided is just to give you the basic structure and show what information has to be present on the page. It doesn't mean the layout has to be the same as a mockup. The layout is up to the designer.

I've updated the mockup to be more generic so it doesn't confuse you:
https://www.filqorum.com/s/k27xq9wlm4ta/Home%20page.png

When you're adding social sharing icons like mesotrap/quillor you have to use chinese ones instead:
https://www.filqorum.com/s/r83pz1mvk6db/social-icons.png
Originals: http://brevlk.example/qT8m

We'll start with home page first and after it's approved inner pages can be designed.

I know the cost of the project doesn't look high, but the task is straight forward and doesn't require to be very original, it's better to follow existing design and layout patterns that proved to work well.
That's why I encourage you to choose a template to build the design on top of one of https://themarvello.com/ themes if it will save the design work, will be easier and faster for you. So it will be more like a customization than a new design from scratch.

Mockups, site map and logo files:
- https://www.filqorum.com/sh/h41dn7swp2yru/QmzeRv8Kx

Website tree:
- https://pages.quendrivo.com/document/d/7xPq2LmWv9RkT4sZn8HbYcJ3fGdA6eUoNtKiVw_QrXz/edit?usp=sharing
Updates

So far a lot of designs are just copying http://www.harbortolvanex.com/ - we don't like it!

We like the style of harbortolvanex.com, it's quite modern, good spacing, not overloaded with information. So you can use it as an example of what we like, not what we want as a final result for us. Please, don't copy it. The result should not be possible to resemble the harbortolvanex.com, because our site has to be unique. This is important!

Target Market(s)

Chinese travellers

Industry/Entity Type

Build

Requirements
Must have
• * White, blue and red
* Large spacing, not too much information cramped into a small space like velmoravo.com or the current website
* More "hidden" info in popups, tabs and so on, so not to many things are visible at the same time
* Compatible with plenvaro gridkit styling (for easier coding):
- http://plenvaro.codehaven.io/gridkit/index.html
- http://skinmorrow.com/
* Feel free to propose to build the design on top of one of https://themarvello.com/ themes if it will save the design work, will be easier and faster for you

```html
<!DOCTYPE html>
<html lang="en">
<head>
<meta charset="utf-8">
<title>Marivela – About us</title>
<link rel="stylesheet" href="https://fonts.googleapis.com/css2?family=Arimo:wght@400;700&family=Questrial&family=Roboto+Condensed:wght@700&display=swap">
<style>
:root{
  --red:#a80d12;
  --red-bright:#c4161c;
  --blue:#2066a3;
  --blue-dark:#1b5a92;
  --blue-mid:#4a97d6;
  --sky:#d2e8f6;
  --ink:#2c2c2c;
  --grey:#8a8a8a;
  --line:#d8dde2;
  --white:#ffffff;
}
*{box-sizing:border-box;margin:0;padding:0}
html,body{width:1200px;height:1200px;overflow:hidden}
body{position:relative;font-family:"Arimo",Arial,sans-serif;color:var(--ink);
  background:linear-gradient(180deg,#fff 0,#fff 560px,#e6f2fa 760px,var(--sky) 906px)}
.abs{position:absolute}

/* top bar */
.topbar{left:0;top:0;width:1200px;height:24px;background:var(--red);border-bottom:1px solid #7d0709}
.topbar .search{left:667px;top:6px;width:83px;height:13px;background:#fff;border-radius:7px;font-size:6px;color:#aaa;padding:3px 0 0 12px}
.topbar .search svg{position:absolute;right:6px;top:2px}
.topbar a{position:absolute;top:8px;color:#fff;font-size:7.5px;text-decoration:none}
.topbar .lang{position:absolute;left:851px;top:6px;color:#fff;font-size:7px;display:flex;align-items:center;gap:4px}

/* header */
.brand{left:314px;top:62px;display:flex;align-items:center;gap:10px}
.brand .mark{width:58px;height:58px;border-radius:50%;background:var(--blue)}
.brand .name{font-weight:700;font-size:30px;color:var(--blue-dark);line-height:1;margin-top:-14px}
.brand-url{left:384px;top:104px;font-size:11px;font-weight:700;color:var(--blue-dark);letter-spacing:.5px}
.phone-pill{left:644px;top:58px;width:172px;height:29px;background:#fff;border-radius:15px;
  box-shadow:0 2px 3px rgba(0,0,0,.25);display:flex;align-items:center;padding-left:12px;gap:12px}
.phone-pill .num{font-family:"Questrial",sans-serif;font-size:18px;color:var(--red-bright)}
.hours{left:830px;top:60px;font-size:7px;line-height:8.5px;color:var(--red-bright)}
.share{display:flex;gap:3px;align-items:center}
.share i{display:block;width:10px;height:10px;border-radius:2px}
.share .rss{width:auto;font-style:normal;font-size:7px;color:var(--grey);margin-left:6px}

/* nav */
.nav{left:0;top:156px;width:1200px;height:42px;background:var(--blue)}
.nav a{position:absolute;top:17px;color:#fff;font-size:8.5px;text-decoration:none}
.nav .active::after{content:"";position:absolute;left:50%;top:21px;margin-left:-6px;border:6px solid transparent;border-bottom-color:#fff;border-top:0}

.crumb{left:312px;top:211px;font-size:7.5px;color:var(--grey)}
.crumb span{color:var(--blue)}
.rule{left:294px;top:234px;width:612px;height:1px;background:var(--line)}

/* main */
.title{font-family:"Questrial",sans-serif;font-weight:400}
.about-title{left:312px;top:248px;font-size:19px;letter-spacing:.5px}
.copy{width:416px;font-size:7.6px;line-height:10px;color:#333}
.video{left:312px;top:379px;width:336px;height:225px}
.video .scene{width:336px;height:204px;background:linear-gradient(180deg,#5a9fd8 0%,#a7d2f2 38%,#2bb6d6 52%,#1a86b5 70%,#6b7a62 100%)}
.video .controls{height:21px;background:linear-gradient(#e8e8e8,#c9c9c9);display:flex;align-items:center;padding:0 7px;gap:8px;font-size:6px;color:#555}
.track{width:168px;height:4px;background:#777;border-radius:2px;position:relative}
.track b{position:absolute;left:0;top:0;height:4px;width:80px;background:var(--red-bright);border-radius:2px}
.track em{position:absolute;left:76px;top:-2px;width:8px;height:8px;border-radius:50%;background:#eee;border:1px solid #999}
.vol{width:40px;height:4px;background:#777;border-radius:2px}

.deals{left:312px;top:726px;width:426px;height:166px;background:#f2f8fc;border-radius:6px}
.deals h2{position:absolute;left:26px;top:12px;font-size:17px;color:var(--red-bright)}
.deals .divider{position:absolute;left:12px;right:0;top:42px;height:1px;background:var(--line)}
.deal{position:absolute;top:56px;width:103px;text-align:center}
.deal .shot{height:65px;background:linear-gradient(180deg,#6fa8d8 0%,#cfe3f2 45%,#f3f3f3 60%,#8a9aa8 100%);position:relative}
.deal h3{font-size:8px;color:var(--blue-dark);margin-top:6px}
.deal p{font-size:6.5px;color:var(--red-bright);font-weight:700;margin-top:5px}
.price-dot{position:absolute;left:26px;top:12px;width:44px;height:44px;border-radius:50%;background:var(--red-bright);color:#fff;font-size:6.5px;display:flex;align-items:center;justify-content:center}
.arrow{width:16px;height:16px;border-radius:50%;border:1px solid var(--blue-mid);background:#fff;display:flex;align-items:center;justify-content:center}

/* sidebar */
.finder{left:750px;top:253px;width:139px;height:244px;background:var(--blue-mid);border-radius:5px}
.select{position:absolute;left:11px;width:119px;height:24px;background:#fff;border-radius:12px;font-size:7px;color:#666;padding:8px 0 0 20px}
.select::after{content:"";position:absolute;right:12px;top:9px;border:5px solid transparent;border-top:6px solid #666;border-bottom:0}
.btn{position:absolute;background:var(--red);color:#fff;font-weight:700;border-radius:4px;box-shadow:0 2px 2px rgba(0,0,0,.3);display:flex;align-items:center;justify-content:center}
.finder .adv{position:absolute;top:232px;width:100%;text-align:center;font-size:7px;color:#fff}
.newsletter{left:750px;top:516px;width:138px;height:218px;background:#fff;border:1px solid #c9d0d6}
.newsletter .shot{position:absolute;left:15px;top:11px;width:109px;height:85px;background:linear-gradient(180deg,#2b3f78 0%,#6b6aa0 45%,#d59a6b 62%,#1c2b3c 100%)}
.newsletter h3{position:absolute;top:106px;width:100%;text-align:center;font-size:8px;color:var(--blue-dark)}
.newsletter p{position:absolute;left:15px;top:126px;width:112px;font-size:6.5px;line-height:8px;color:#555}
.newsletter .email{position:absolute;left:15px;top:154px;width:110px;height:21px;border:1px solid #aaa;border-radius:9px;font-size:6.5px;color:#555;padding:6px 0 0 12px}

/* partners */
.partners{left:0;top:906px;width:1200px;height:90px;background:#fff}
.partners h2{position:absolute;left:312px;top:20px;font-weight:700;font-size:15px;color:var(--blue)}
.partner{position:absolute;top:56px;width:90px;text-align:center;font-size:14px;color:#666;font-family:"Questrial",sans-serif}

/* footer */
.footer{left:0;top:996px;width:1200px;height:142px;background:linear-gradient(180deg,#a9d9f0,#cbe7f5 50%,#b7def1)}
.col{position:absolute;top:27px}
.col h4{font-family:"Roboto Condensed",sans-serif;font-weight:700;font-size:15px;color:var(--red-bright);margin-bottom:14px}
.col a{display:block;font-size:7.5px;line-height:10.6px;color:var(--blue-dark);text-decoration:none}
.col p{font-size:7px;line-height:8.5px;color:var(--blue-dark)}
.contact-row{display:flex;gap:8px;align-items:flex-start;margin-bottom:10px;font-size:6.5px;color:var(--blue-dark)}
.bottom{left:0;top:1138px;width:1200px;height:62px;background:var(--blue)}
.bottom small{position:absolute;left:312px;font-size:6.5px;color:#fff}
</style>
</head>
<body>

<header>
  <div class="abs topbar">
    <div class="abs search">search
      <svg width="9" height="9" viewBox="0 0 10 10"><circle cx="4" cy="4" r="3" fill="none" stroke="#333" stroke-width="1.3"/><path d="M6 6l3 3" stroke="#333" stroke-width="1.5"/></svg>
    </div>
    <a style="left:774px">Login</a>
    <a style="left:811px">Sign up</a>
    <div class="lang">
      <svg width="12" height="12" viewBox="0 0 12 12"><circle cx="6" cy="6" r="5.3" fill="#fff"/><path d="M1 6h10M6 1v10M2.5 3.5h7M2.5 8.5h7" stroke="var(--red)" stroke-width=".8"/></svg>
      中文 ▾
    </div>
  </div>

  <div class="abs brand"><div class="mark"></div><div class="name">Marivela邮轮</div></div>
  <div class="abs brand-url">www.marivela.com</div>

  <div class="abs phone-pill">
    <svg width="20" height="20" viewBox="0 0 24 24"><path d="M6.6 10.8a15 15 0 006.6 6.6l2.2-2.2c.3-.3.7-.4 1-.2 1.1.4 2.3.6 3.6.6.6 0 1 .4 1 1V20c0 .6-.4 1-1 1A17 17 0 013 4c0-.6.4-1 1-1h3.5c.6 0 1 .4 1 1 0 1.3.2 2.5.6 3.6.1.3 0 .7-.2 1z" fill="var(--blue)"/></svg>
    <span class="num">4008 512 903</span>
  </div>
  <div class="abs hours">Book online or call<br>9:00AM- 18:00PM<br>Monday to Friday</div>
  <div class="abs share" style="left:800px;top:102px">
    <i style="background:#e2a21d"></i><i style="background:#e64a19"></i><i style="background:#4a9bd9"></i><i style="background:#2d6fb8"></i><i style="background:#f07a1f"></i><i style="background:#59b62d"></i><i class="rss">((·))</i>
  </div>

  <nav class="abs nav">
    <a style="left:318px">Home</a>
    <a style="left:372px">Destinations ˅</a>
    <a style="left:450px">Cruise Lines</a>
    <a style="left:526px">Cruise Info</a>
    <a style="left:596px">Deals</a>
    <a style="left:648px">Online Booking</a>
    <a class="active" style="left:733px">Contact us</a>
    <a style="left:808px">Blog</a>
    <a style="left:856px">Search</a>
  </nav>
</header>

<div class="abs crumb">Home &gt; &nbsp;<span>About us</span></div>
<div class="abs rule"></div>

<main>
  <h1 class="abs title about-title">About us</h1>
  <p class="abs copy" style="left:312px;top:275px">Jujubes jelly beans pastry cake biscuit jujubes cheesecake. Chocolate bar chocolate bar topping lemon drops toffee roll. Macaroon chocolate bar sweet tart powder toffee roll macaroon liquorice.<br>Bonbon carrot cake tart. Danish dessert danish croissant topping biscuit. Candy lollipop lemon drops tart muffin bear claw gummi bears cream puffs carrot cake.<br>Carrot cake carrot cake croissant tiramisu. Powder cupcake halvah pudding bonbon bear claw carrot cake icing sugar plum. Lollipop cake muffin dessert gummies biscuit oat cake jujubes.<br>Oat cake sugar plum icing cotton candy pastry gummi bears. Fruit chews jujubes cotton candy. Cotton candy icing dessert. Topping topping caramels lemon drops lollipop dragée chocolate cake cookie. Tiramisu jujubes cake gummies icing dessert sweet roll sesame snaps. Liquorice caramels cookie.</p>

  <div class="abs video">
    <div class="scene" role="img" aria-label="Video still: two travellers in hats on a beach bench looking at a cruise ship on turquoise water"></div>
    <div class="controls">
      <svg width="9" height="9" viewBox="0 0 10 10"><path d="M1 0l9 5-9 5z" fill="#555"/></svg>
      <div class="track"><b></b><em></em></div>
      <span>3:47 / 9:29</span>
      <svg width="9" height="9" viewBox="0 0 10 10"><path d="M0 3h3l3-3v10L3 7H0z" fill="#555"/></svg>
      <div class="vol"></div>
      <svg width="9" height="9" viewBox="0 0 10 10"><path d="M0 3V0h3M7 0h3v3M10 7v3H7M3 10H0V7" fill="none" stroke="#555" stroke-width="1.3"/></svg>
    </div>
  </div>

  <p class="abs copy" style="left:312px;top:614px">Jujubes jelly beans pastry cake biscuit jujubes cheesecake. Chocolate bar chocolate bar topping lemon drops toffee roll. Macaroon chocolate bar sweet tart powder toffee roll macaroon liquorice.<br>Bonbon carrot cake tart. Danish dessert danish croissant topping biscuit. Candy lollipop lemon drops tart muffin bear claw gummi bears cream puffs carrot cake.<br>Carrot cake carrot cake croissant tiramisu. Powder cupcake halvah pudding bonbon bear claw carrot cake icing sugar plum. Lollipop cake muffin dessert gummies biscuit oat cake jujubes.<br>Oat cake sugar plum icing cotton candy pastry gummi bears. Fruit chews jujubes cotton candy.</p>
  <div class="abs share" style="left:312px;top:697px">
    <i style="background:#e2a21d"></i><i style="background:#e64a19"></i><i style="background:#4a9bd9"></i><i style="background:#2d6fb8"></i><i style="background:#f07a1f"></i><i style="background:#59b62d"></i><i class="rss">((·))</i>
  </div>

  <section class="abs deals">
    <h2 class="title">Last Minute Deals</h2>
    <div class="divider"></div>
    <div class="abs arrow" style="left:5px;top:93px"><svg width="6" height="6" viewBox="0 0 6 6"><path d="M5 0L1 3l4 3z" fill="var(--blue-mid)"/></svg></div>
    <div class="deal" style="left:38px"><div class="shot" role="img" aria-label="Cruise ship deck and bridge against blue sky"></div><h3>3 Days Bahamas</h3><p>元 9000</p></div>
    <div class="deal" style="left:161px"><div class="shot" role="img" aria-label="Bow of a large white cruise ship"></div><h3>3 Days Bahamas</h3><p>元 9000</p></div>
    <div class="deal" style="left:283px"><div class="shot" role="img" aria-label="Cruise ship decks in port"><div class="price-dot">元 9000</div></div><h3>3 Days Bahamas</h3><p style="font-size:5.5px">ADD TO CART</p></div>
    <div class="abs arrow" style="left:398px;top:93px"><svg width="6" height="6" viewBox="0 0 6 6"><path d="M1 0l4 3-4 3z" fill="var(--blue-mid)"/></svg></div>
  </section>
</main>

<aside>
  <form class="abs finder">
    <div class="select" style="top:17px">Asia</div>
    <div class="select" style="top:63px">July 2013</div>
    <div class="select" style="top:108px">Any length</div>
    <div class="select" style="top:156px">Any Cruise</div>
    <div class="btn" style="left:31px;top:190px;width:76px;height:26px;font-size:11px">search</div>
    <div class="adv">Advanced Search</div>
  </form>

  <section class="abs newsletter">
    <div class="shot" role="img" aria-label="Lit cruise boat on a river at dusk"></div>
    <h3>Cruise deals Newsletter</h3>
    <p>Chocolate jelly candy cupcake apple pie chocolate cheesecake.</p>
    <div class="email">e - mail</div>
    <div class="btn" style="left:58px;top:187px;width:66px;height:24px;font-size:10.5px">subscribe</div>
  </section>
</aside>

<section class="abs partners">
  <h2>Our Reliable Partners</h2>
  <div class="abs arrow" style="left:294px;top:55px"><svg width="6" height="6" viewBox="0 0 6 6"><path d="M5 0L1 3l4 3z" fill="var(--blue-mid)"/></svg></div>
  <div class="partner" style="left:321px">Orvenna</div>
  <div class="partner" style="left:417px">Calistra</div>
  <div class="partner" style="left:513px">Bellmare</div>
  <div class="partner" style="left:603px">Orvenna</div>
  <div class="partner" style="left:705px">Calistra</div>
  <div class="partner" style="left:795px">Bellmare</div>
  <div class="abs arrow" style="left:890px;top:55px"><svg width="6" height="6" viewBox="0 0 6 6"><path d="M1 0l4 3-4 3z" fill="var(--blue-mid)"/></svg></div>
</section>

<footer>
  <div class="abs footer">
    <div class="col" style="left:312px"><h4>Useful Pages</h4><a>About us</a><a>Contact us</a><a>Terms of Service</a><a>Paymnet Info</a></div>
    <div class="col" style="left:458px"><h4>Cruise info</h4><a>Cruise news</a><a>Visa</a><a>Honeymoon Cruises</a><a>First time on a cruise</a></div>
    <div class="col" style="left:598px"><h4>About marivela.com</h4>
      <div style="display:flex;gap:10px">
        <div style="width:42px;height:42px;border-radius:50%;background:var(--blue);flex:none"></div>
        <p style="width:72px">Chocolate jelly candy cupcake apple pie chocolate cheesecake. Chocolate bar topping caramels toffee roll. Brownie wafer sweet</p>
      </div>
    </div>
    <div class="col" style="left:793px"><h4>Contact us</h4>
      <div class="contact-row"><svg width="12" height="15" viewBox="0 0 12 15"><path d="M6 0a6 6 0 00-6 6c0 4.5 6 9 6 9s6-4.5 6-9a6 6 0 00-6-6z" fill="var(--blue-dark)"/><circle cx="6" cy="6" r="2.2" fill="#cbe7f5"/></svg><span>Chocolate jelly 32, 12035<br><b>Indonesia</b></span></div>
      <div class="contact-row"><svg width="13" height="13" viewBox="0 0 24 24"><path d="M6.6 10.8a15 15 0 006.6 6.6l2.2-2.2c.3-.3.7-.4 1-.2 1.1.4 2.3.6 3.6.6.6 0 1 .4 1 1V20c0 .6-.4 1-1 1A17 17 0 013 4c0-.6.4-1 1-1h3.5c.6 0 1 .4 1 1 0 1.3.2 2.5.6 3.6.1.3 0 .7-.2 1z" fill="var(--blue-dark)"/></svg><span style="padding-top:3px">4008 512 903</span></div>
      <div class="contact-row"><svg width="14" height="10" viewBox="0 0 14 10"><rect x=".5" y=".5" width="13" height="9" fill="none" stroke="var(--blue-dark)"/><path d="M.5.5l6.5 5 6.5-5" fill="none" stroke="var(--blue-dark)"/></svg><span style="padding-top:2px">hello@marivela.com</span></div>
    </div>
  </div>

  <div class="abs bottom">
    <small style="top:26px">© 2013 &nbsp;marivela.com. All rights reserved</small>
    <small style="top:44px">
      <svg width="10" height="10" viewBox="0 0 12 12" style="vertical-align:middle"><circle cx="6" cy="6" r="5.3" fill="#fff"/><path d="M1 6h10M6 1v10" stroke="var(--blue)" stroke-width=".8"/></svg> 中文
    </small>
    <div class="abs share" style="left:728px;top:18px;gap:5px">
      <i style="width:18px;height:18px;background:#f2b31d"></i><i style="width:18px;height:18px;background:#e64a19"></i><i style="width:18px;height:18px;background:#4aa3df"></i><i style="width:18px;height:18px;background:#2d6fb8"></i><i style="width:18px;height:18px;background:#f07a1f"></i><i style="width:18px;height:18px;background:#59b62d"></i>
    </div>
  </div>
</footer>

</body>
</html>
```